Email signature design - law firm

We are a small boutique law firm which is located near the beach in Manly, Australia.

We have just recently developed a new logo and are looking to redesign our letterhead, business cards and email signatures.

This brief is for our email signatures. This is an email signature to appear at the bottom of our Outlook emails so we would like it to be text that we are able to edit as the wording in our email signature often required amendments.

I have attached a word document which had our new logo, and our previous email signature which all the information/wording that needs to be included.

We would like multiple designs with a modern, simplistic yet striking look.

Thanks.

font - raleway or montserrat

Need extra days to review

• Must have the exact wording which appears in the email signature in the word document attached to brief.
• Must be able to edit the text as it is for an Outlook email signature which wording will change from time to time.

```html
<!DOCTYPE html>
<html lang="en">
<head>
<meta charset="utf-8">
<title>Harlow &amp; Partners – Stationery</title>
<link href="https://fonts.googleapis.com/css2?family=Raleway:wght@400;500;600;700&display=swap" rel="stylesheet">
<style>
  :root {
    --stage: #2e2e30;
    --paper: #ffffff;
    --navy: #2b3a8c;
    --ocean: #3a6fb8;
    --sand: #d4a246;
    --ink: #4a4f63;
    --mist: #e6e7ea;
    --rule: #c9ccd6;
  }
  * { margin: 0; padding: 0; box-sizing: border-box; }
  html, body { width: 800px; height: 1200px; overflow: hidden; }
  body {
    background: var(--stage);
    font-family: "Raleway", sans-serif;
    color: var(--ink);
    position: relative;
  }

  /* Letterhead */
  .letterhead {
    position: absolute;
    left: 147px; top: 120px;
    width: 506px; height: 758px;
    background: var(--paper);
  }
  .letterhead__brand {
    position: absolute;
    top: 22px; left: 0; right: 0;
    display: flex; align-items: center; justify-content: center; gap: 8px;
    font-size: 17px; font-weight: 700; color: var(--navy);
  }
  .brand-dot {
    width: 12px; height: 12px; border-radius: 50%;
    background: var(--ocean);
  }
  .letterhead__watermark {
    position: absolute;
    top: 300px; left: 40px; right: 40px;
    text-align: center;
    font-size: 56px; font-weight: 700;
    color: var(--mist);
    line-height: 1.1;
  }
  .letterhead__footer {
    position: absolute;
    left: 18px; right: 18px; top: 700px;
    font-size: 10.5px; line-height: 17px; color: var(--ink);
  }
  .letterhead__footer .firm { color: var(--navy); font-weight: 700; margin-right: 4px; }
  .letterhead__footer .web { color: var(--ocean); font-weight: 600; }
  .letterhead__band {
    position: absolute; left: 0; right: 0; bottom: 0;
    height: 12px; background: var(--navy);
  }
  .letterhead__band::before {
    content: ""; position: absolute; left: 0; right: 0; top: -5px;
    height: 2px; background: var(--navy);
  }

  /* Email signature */
  .signature {
    position: absolute;
    left: 147px; top: 965px;
    width: 506px; height: 155px;
    background: var(--paper);
  }
  .signature__greeting {
    position: absolute; left: 18px; top: 12px;
    font-size: 11px; color: var(--ocean);
  }
  .signature__name {
    position: absolute; left: 18px; top: 25px;
    font-size: 17px; font-weight: 600; color: var(--navy);
  }
  .signature__rule {
    position: absolute; left: 18px; right: 18px; height: 1px; background: var(--rule);
  }
  .signature__rule--top { top: 50px; }
  .signature__rule--mid { top: 113px; left: 150px; }
  .signature__brand {
    position: absolute; left: 18px; top: 66px;
    display: flex; align-items: center; gap: 6px;
    font-size: 12px; font-weight: 700; color: var(--navy);
  }
  .signature__brand .brand-dot { width: 9px; height: 9px; }
  .signature__details {
    position: absolute; left: 150px; top: 58px;
    font-size: 10.5px; line-height: 13.5px; color: var(--ink);
  }
  .signature__details .firm { color: var(--navy); font-weight: 700; }
  .signature__details .web { color: var(--ocean); font-weight: 600; }
  .signature__social {
    position: absolute; left: 150px; top: 120px;
    display: flex; align-items: center; gap: 4px;
    font-size: 10px; color: var(--ink);
  }
  .social-dot { width: 11px; height: 11px; border-radius: 50%; background: var(--ocean); }
  .signature__social .handle { margin-left: 3px; }
  .signature__band {
    position: absolute; left: 0; right: 0; bottom: 0;
    height: 9px; background: var(--navy);
  }
</style>
</head>
<body>
  <section class="letterhead">
    <div class="letterhead__brand"><span class="brand-dot"></span>Harlow &amp; Partners</div>
    <div class="letterhead__watermark" aria-hidden="true">Harlow &amp;<br>Partners</div>
    <div class="letterhead__footer">
      <p><span class="firm">HARLOW &amp; PARTNERS</span> Suite 4, 12 Harbour Lane, MANLY &nbsp; NSW &nbsp;2095</p>
      <p>P: (02) 9000 1234 | F: (02) 9000 1235 | <span class="web">www.harlowpartners.com.au</span></p>
    </div>
    <div class="letterhead__band"></div>
  </section>

  <section class="signature">
    <p class="signature__greeting">Regards</p>
    <p class="signature__name">Maya Bennett</p>
    <div class="signature__rule signature__rule--top"></div>
    <div class="signature__brand"><span class="brand-dot"></span>Harlow &amp; Partners</div>
    <div class="signature__details">
      <p class="firm">Harlow &amp; Partners</p>
      <p>Suite 4, 12 Harbour Lane, MANLY &nbsp;NSW &nbsp;2095</p>
      <p>P: (02) 9000 1234 | F: (02) 9000 1235</p>
      <p class="web">www.harlowpartners.com.au</p>
    </div>
    <div class="signature__rule signature__rule--mid"></div>
    <div class="signature__social">
      <span>Follow us on:</span>
      <span class="social-dot"></span><span class="social-dot"></span><span class="social-dot"></span><span class="social-dot"></span><span class="social-dot"></span>
      <span class="handle">/ name</span>
    </div>
    <div class="signature__band"></div>
  </section>
</body>
</html>
```